Keyvane - Premium Club Brochure

Up until now, we've used Canva to create the Brochure we have at-hand, the one attached to this enquiry.

I have been referred to DraftHive by my Business Partner, Marcus Penrovey.

We have recently established a New Real Estate Agency.

This Brochure is our Property Management Membership Brochure, describing the 3x Memberships (Gold, Platinum & Diamond) & outlining the Benefits & Bonuses that are included in these Memberships.

For ALL Pages, we are open to suggestions & other designs/templates/colour schemes.

Target Market(s)

Real Estate - Landlords / Investors

Industry/Entity Type

Real Estate

Font styles to use
Serif
Sans Serif

Colors

Designer to choose colors to be used in the design.

Requirements
Must have
• We would like to do the following:
• - Page 1:
• 1. Include under Email: info@keyvane-demo.com.au
• 2. Include Website under Email (www.keyvane-demo.com.au).
• Website
• www.keyvane-demo.com.au
• 3. The Picture on the right, could we change that Photo to a Block of Apartments & remove the Lines going across the Picture.
• - Page 2
• 1. Create a Border around the Page.
• 2. Heading - Make it stand out more.
• 3. Create Banners for 'Quality Service' & '2.5% Lowest Fees'.
• 4. Categorise the Memberships with these Boarders, please refer to the attachment for example.
• 5. Annual Savings - Make it stand out more.
• - Page 3
• - Page 4
• Please for ALL Fonts, make them the same, we do NOT have the correct font programs to unify them.
Nice to have
• - Page 1:
• Website
• www.keyvane-demo.com.au
• - Page 2:
• When it mentions "2.5% Lowest Fees', please feel free to provide any suggestions, we are open to any suggestions/ideas for this.
Should not have
• Grammar or Spelling errors.

```html
<!DOCTYPE html>
<html lang="en">
<head>
<meta charset="utf-8">
<title>Keyvane – Premium Membership Club Brochure</title>
<link rel="stylesheet" href="https://fonts.googleapis.com/css2?family=Open+Sans:wght@300;400;600;700;800&display=swap">
<style>
  :root{
    --stage:#e4e4e4;
    --ink:#1d1d1d;
    --ink-deep:#111111;
    --ink-soft:#2b2b2b;
    --yellow:#f2c200;
    --lime:#e4e21a;
    --text:#f2f2f2;
    --text-muted:#c9c9c9;
    --photo-sky:#8c8f8a;
    --photo-house:#cfc6b4;
  }
  *{box-sizing:border-box;margin:0;padding:0}
  html,body{width:1200px;height:824px;overflow:hidden;background:var(--stage)}
  body{font-family:"Open Sans",Arial,sans-serif;color:var(--text)}
  .spread{position:absolute;left:50px;top:22px;width:1100px;height:780px;display:flex;box-shadow:0 12px 30px rgba(0,0,0,.25)}
  .page{position:relative;width:550px;height:780px;overflow:hidden;background:var(--ink)}
  .page-art{position:absolute;inset:0;width:100%;height:100%}

  /* back cover */
  .disclaimer{position:absolute;left:48px;top:92px;width:460px}
  .disclaimer-title{font-size:21px;font-weight:800;letter-spacing:.3px;text-transform:uppercase;color:#fff;margin-bottom:12px}
  .disclaimer-title .accent{color:var(--yellow)}
  .terms{list-style:none}
  .terms li{position:relative;padding-left:16px;font-size:9.6px;line-height:1.45;color:var(--text-muted);margin-bottom:3px}
  .terms li svg{position:absolute;left:0;top:3px;width:9px;height:8px}

  .contact{position:absolute;left:0;right:0;top:640px;text-align:center}
  .contact-title{font-size:17px;font-weight:400;letter-spacing:.5px;color:#fff}
  .contact-title .accent{font-weight:800;color:var(--yellow)}
  .contact-rule{width:44px;height:2px;background:var(--yellow);margin:6px auto 10px}
  .contact-line{font-size:10.5px;color:var(--text-muted);line-height:1.6;display:flex;justify-content:center;align-items:center;gap:6px}
  .contact-line svg{width:10px;height:10px;flex:none}
  .contact-line .gap{width:12px}

  /* front cover */
  .brand{position:absolute;left:0;right:0;top:62px;text-align:center;font-size:34px;font-weight:300;letter-spacing:16px;padding-left:16px;color:#fff}
  .cover-title{position:absolute;left:0;right:0;top:560px;text-align:center;font-size:30px;font-weight:300;line-height:1.2;color:#fff}
  .cover-rule{position:absolute;left:250px;top:642px;width:50px;height:2px;background:var(--yellow)}
  .cover-contacts{position:absolute;left:40px;right:40px;top:662px;height:40px;border:1px solid var(--yellow);border-radius:20px;display:flex;justify-content:center;align-items:center;gap:26px;font-size:12px;color:#fff}
  .cover-contacts span{display:flex;align-items:center;gap:7px}
  .cover-contacts svg{width:12px;height:12px}
</style>
</head>
<body>
<div class="spread">

  <!-- Back cover -->
  <section class="page page-back">
    <svg class="page-art" viewBox="0 0 550 780" preserveAspectRatio="none">
      <defs>
        <linearGradient id="backPhoto" x1="0" y1="0" x2="0" y2="1">
          <stop offset="0" stop-color="#2a2a2a"/>
          <stop offset="1" stop-color="#1b1b1b"/>
        </linearGradient>
        <linearGradient id="swoosh" x1="0" y1="0" x2="1" y2="0">
          <stop offset="0" stop-color="var(--lime)"/>
          <stop offset="1" stop-color="var(--yellow)"/>
        </linearGradient>
      </defs>
      <rect width="550" height="780" fill="var(--ink)"/>
      <path d="M0 0 H550 V470 Q300 560 0 610 Z" fill="url(#backPhoto)" opacity=".9" role="img" aria-label="Faint darkened photo of a suburban house behind the disclaimer text"/>
      <path d="M0 610 Q300 560 550 470 V780 H0 Z" fill="var(--ink-soft)"/>
      <path d="M0 612 Q300 562 550 468 L550 476 Q300 568 0 616 Z" fill="url(#swoosh)"/>
    </svg>

    <div class="disclaimer">
      <h2 class="disclaimer-title">Premium Club <span class="accent">Disclaimer</span></h2>
      <ul class="terms">
        <li><svg viewBox="0 0 10 8"><path d="M1 4l3 3 5-6" fill="none" stroke="#f2c200" stroke-width="1.6"/></svg>Keyvane Group Pty Ltd is a FULLY Licensed Real Estate Agent.</li>
        <li><svg viewBox="0 0 10 8"><path d="M1 4l3 3 5-6" fill="none" stroke="#f2c200" stroke-width="1.6"/></svg>Keyvane Group &amp; its subsidiary Businesses operate under the 1 &amp; same ABN.</li>
        <li><svg viewBox="0 0 10 8"><path d="M1 4l3 3 5-6" fill="none" stroke="#f2c200" stroke-width="1.6"/></svg>Memberships can be upgraded with a written Notice issued to Keyvane Group, upgrade will take into affect after 1-Month.</li>
        <li><svg viewBox="0 0 10 8"><path d="M1 4l3 3 5-6" fill="none" stroke="#f2c200" stroke-width="1.6"/></svg>Memberships can be cancelled with a written Notice issued to Keyvane Group, cancellation will take into affect after 1-Month &amp; a FULL Refund of Membership Fees will be made (only applicable to Platinum and Diamond Membership).</li>
        <li><svg viewBox="0 0 10 8"><path d="M1 4l3 3 5-6" fill="none" stroke="#f2c200" stroke-width="1.6"/></svg>Keyvane Consultation &amp; Advisory Services are of Information Sharing basis and Client MUST conduct their own enquiries with the relevant Qualified Professionals.</li>
        <li><svg viewBox="0 0 10 8"><path d="M1 4l3 3 5-6" fill="none" stroke="#f2c200" stroke-width="1.6"/></svg>Keyvane Group's Affiliated &amp; Referred Professionals are deemed to be properly qualified and Client MUST verify on their own discretion &amp; accord.</li>
        <li><svg viewBox="0 0 10 8"><path d="M1 4l3 3 5-6" fill="none" stroke="#f2c200" stroke-width="1.6"/></svg>Keyvane Group CANNOT be held accountable and/or responsible for the actions of other Entities.</li>
        <li><svg viewBox="0 0 10 8"><path d="M1 4l3 3 5-6" fill="none" stroke="#f2c200" stroke-width="1.6"/></svg>ALL Benefits are subject to Terms &amp; Conditions of KEYVANE Premium Club.</li>
        <li><svg viewBox="0 0 10 8"><path d="M1 4l3 3 5-6" fill="none" stroke="#f2c200" stroke-width="1.6"/></svg>Terms &amp; Conditions will be issued to every Member and available on Keyvane Website: www.keyvane-demo.com.au</li>
        <li><svg viewBox="0 0 10 8"><path d="M1 4l3 3 5-6" fill="none" stroke="#f2c200" stroke-width="1.6"/></svg>ALL Benefits &amp; Bonuses are ONLY applicable to Residential Properties.</li>
        <li><svg viewBox="0 0 10 8"><path d="M1 4l3 3 5-6" fill="none" stroke="#f2c200" stroke-width="1.6"/></svg>Bank Valuation/s are subject to Bank/s' discretion &amp; may NOT be provided as Hard-Copy.</li>
        <li><svg viewBox="0 0 10 8"><path d="M1 4l3 3 5-6" fill="none" stroke="#f2c200" stroke-width="1.6"/></svg>Benefits and Bonuses may be amended with Notice. Membership Fee/s are FULLY Refunded &amp; guaranteed by Keyvane Group Pty Ltd. ALL Benefits &amp; Bonuses are to be terminated on the day of Notice &amp; NO Pro-Rata will be given.</li>
      </ul>
    </div>

    <div class="contact">
      <h3 class="contact-title">CONTACT <span class="accent">INFO</span></h3>
      <div class="contact-rule"></div>
      <p class="contact-line"><svg viewBox="0 0 10 10"><path d="M5 9.5C3 7 2 5.5 2 4a3 3 0 0 1 6 0c0 1.5-1 3-3 5.5z" fill="#f2c200"/></svg>Level 9 Harbourline House, 42 Wattlebrook Road<span class="gap"></span><svg viewBox="0 0 10 10"><path d="M2 1l2 .5.5 2-1 1a6 6 0 0 0 2 2l1-1 2 .5.5 2C5 9 1 5 2 1z" fill="#f2c200"/></svg>(02)5550 1437</p>
      <p class="contact-line">Calderwood Nsw 2199</p>
      <p class="contact-line"><svg viewBox="0 0 10 10"><rect x="1" y="2.5" width="8" height="5.5" fill="none" stroke="#f2c200"/><path d="M1 2.5l4 3 4-3" fill="none" stroke="#f2c200"/></svg>info@keyvane-demo.com.au</p>
      <p class="contact-line"><svg viewBox="0 0 10 10"><circle cx="5" cy="5" r="4" fill="none" stroke="#f2c200"/><path d="M1 5h8M5 1c2 2 2 6 0 8M5 1c-2 2-2 6 0 8" fill="none" stroke="#f2c200" stroke-width=".8"/></svg>www.keyvane-demo.com.au</p>
    </div>
  </section>

  <!-- Front cover -->
  <section class="page page-front">
    <svg class="page-art" viewBox="0 0 550 780" preserveAspectRatio="none">
      <defs>
        <linearGradient id="housePhoto" x1="0" y1="0" x2="0" y2="1">
          <stop offset="0" stop-color="var(--photo-sky)"/>
          <stop offset=".55" stop-color="var(--photo-house)"/>
          <stop offset="1" stop-color="#8a7a62"/>
        </linearGradient>
        <linearGradient id="coverSwoosh" x1="0" y1="0" x2="1" y2="0">
          <stop offset="0" stop-color="var(--yellow)"/>
          <stop offset=".5" stop-color="var(--lime)"/>
          <stop offset="1" stop-color="var(--yellow)"/>
        </linearGradient>
        <linearGradient id="coverLower" x1="0" y1="0" x2="0" y2="1">
          <stop offset="0" stop-color="var(--ink-soft)"/>
          <stop offset="1" stop-color="var(--ink)"/>
        </linearGradient>
      </defs>
      <rect width="550" height="780" fill="var(--ink-deep)"/>
      <path d="M0 175 Q300 150 550 130 V445 Q300 470 0 530 Z" fill="url(#housePhoto)" role="img" aria-label="Photo of a two-storey weatherboard family house with dark shutters and bare trees"/>
      <path d="M0 530 Q300 470 550 445 V780 H0 Z" fill="url(#coverLower)"/>
      <path d="M0 530 Q300 470 550 445 L550 462 Q300 488 0 546 Z" fill="url(#coverSwoosh)"/>
    </svg>

    <div class="brand">KEYVANE</div>
    <h1 class="cover-title">Premium<br>Membership Club</h1>
    <div class="cover-rule"></div>
    <div class="cover-contacts">
      <span><svg viewBox="0 0 10 10"><rect x="1" y="2.5" width="8" height="5.5" fill="none" stroke="#f2c200"/><path d="M1 2.5l4 3 4-3" fill="none" stroke="#f2c200"/></svg>info@keyvane-demo.com.au</span>
      <span><svg viewBox="0 0 10 10"><circle cx="5" cy="5" r="4" fill="none" stroke="#f2c200"/><path d="M1 5h8M5 1c2 2 2 6 0 8M5 1c-2 2-2 6 0 8" fill="none" stroke="#f2c200" stroke-width=".8"/></svg>www.keyvane-demo.com.au</span>
    </div>
  </section>

</div>
</body>
</html>
```